Specialized tax accounting firm needs letterhead design

We need a letterhead design for a professional services firm called R. Desmond Pell Inc. The firm is essentially a very specialized tax accounting firm - instead of serving the end consumer, we support other public accounting firms in the area of Canadian and U.S. tax advisory and compliance (i.e. they call us on tax issues too complex for the general practitioner. Our byline is "Tax Support Services for Public Accounting Firms". Our letterhead should utilize our logo and be based on colours present in our logo (see file attached). The final design needs to convey professionalism and trustworthiness (we're hired by accountants after all!) while being creative and eye-catching.

I've attached:
The font used in the logo
The logo itself in a variety of file formats
A single page showing the key firm information which should be appearing in the letterhead

Please note that there is much more leather background around the logo than needs to be incorporated in the letterhead.

Industry/Entity Type

Accounting

```html
<!DOCTYPE html>
<html lang="en">
<head>
<meta charset="utf-8">
<title>R. Desmond Pell Inc. — Letterhead</title>
<link rel="stylesheet" href="https://fonts.googleapis.com/css2?family=Cinzel:wght@400;700&display=swap">
<style>
  :root {
    --brand-blue: #1b6fc0;
    --brand-blue-dark: #13549a;
    --brand-orange: #f39a1e;
    --paper: #ffffff;
    --ink-light: #ffffff;
    --watermark: rgba(90, 100, 120, 0.09);
    --watermark-mark: rgba(243, 154, 30, 0.12);
  }
  * { margin: 0; padding: 0; box-sizing: border-box; }
  html, body { width: 849px; height: 1200px; overflow: hidden; background: var(--paper); }
  .letterhead {
    position: relative;
    width: 849px;
    height: 1200px;
    background: var(--paper);
    overflow: hidden;
    font-family: "Cinzel", "Times New Roman", serif;
  }
  .header-shapes { position: absolute; top: 0; left: 0; }
  .firm-name {
    position: absolute;
    top: 14px;
    left: 0;
    width: 849px;
    text-align: center;
    color: var(--ink-light);
    font-size: 50px;
    font-weight: 400;
    letter-spacing: 6px;
    line-height: 1;
  }
  .byline {
    position: absolute;
    top: 72px;
    left: 80px;
    color: var(--ink-light);
    font-size: 17px;
    letter-spacing: 2px;
    line-height: 1;
  }
  .watermark {
    position: absolute;
    top: 0; left: 0;
    width: 849px; height: 1200px;
    pointer-events: none;
  }
  .watermark-mark {
    position: absolute;
    top: 215px;
    left: 20px;
    width: 150px;
    height: 150px;
    background: var(--watermark-mark);
  }
  .watermark-text {
    position: absolute;
    top: 560px;
    left: -10px;
    width: 960px;
    transform: rotate(40deg);
    transform-origin: center;
    color: var(--watermark);
    text-align: center;
    line-height: 1;
  }
  .watermark-name { font-size: 110px; letter-spacing: 8px; white-space: nowrap; }
  .watermark-byline { font-size: 30px; letter-spacing: 4px; margin-top: 14px; white-space: nowrap; }
  .footer-band {
    position: absolute;
    left: 0; bottom: 0;
    width: 849px;
    height: 84px;
    background: var(--brand-blue);
    color: var(--ink-light);
    text-align: center;
  }
  .footer-address {
    margin-top: 20px;
    font-size: 17px;
    letter-spacing: 2px;
    font-weight: 700;
  }
  .footer-contact {
    margin-top: 10px;
    font-size: 11px;
    letter-spacing: 1.2px;
  }
</style>
</head>
<body>
  <main class="letterhead">
    <svg class="header-shapes" width="849" height="160" viewBox="0 0 849 160" aria-hidden="true">
      <polygon points="0,0 849,0 849,92 90,92 0,60" fill="var(--brand-blue)"/>
      <polygon points="0,60 90,92 849,92 849,100 110,100 0,72" fill="var(--brand-blue-dark)"/>
      <polygon points="335,108 849,108 849,156 305,156" fill="var(--brand-orange)"/>
    </svg>

    <h1 class="firm-name">R. Desmond Pell Inc</h1>
    <p class="byline">Tax Support Services for Public Accounting Firms</p>

    <div class="watermark" aria-hidden="true">
      <div class="watermark-mark"></div>
      <div class="watermark-text">
        <div class="watermark-name">R. Desmond Pell</div>
        <div class="watermark-byline">Tax Support Services for Public Accounting Firms</div>
      </div>
    </div>

    <footer class="footer-band">
      <p class="footer-address">18-412 Harbourview Road, Halifax, Nova Scotia, Canada B3K 2R7</p>
      <p class="footer-contact">Phone 902.555.0148 &middot; Fax 902.555.0149 &middot; desmond@pelltaxsupport.ca &middot; www.pelltaxsupport.ca</p>
    </footer>
  </main>
</body>
</html>
```